New Business Card Design Project

New business card design required for an electrical business in Australia. Offering quality electrical services including design and installation. Electrical services offered are domestic, commercial and industrial. Also meets all the air conditioning installation and maintenance needs.

Target Market(s)

The business is sleek, professional and caters primarily to wealthy clients and government contracts looking for exceptional, tailored service.

Industry/Entity Type

Electrical

Contact Information for Business Card

Gareth Pollwick (Director)
0438 692 174
admin@rvoelectrical.com.au
www.rvoelectrical.com.au

Font styles to use
Sans Serif

Requirements
Must have
• The business card must show the license number - 64139 to comply with legislation.
Nice to have
• The logo colours and fonts could be incorporated into the design if the designer sees fit. We are open to new ideas and welcome creativity. The logo style guide is attached for reference if required.

```html
<!DOCTYPE html>
<html lang="en">
<head>
<meta charset="utf-8">
<title>RVO Electrical – Business Card</title>
<link rel="stylesheet" href="https://fonts.googleapis.com/css2?family=Arimo:wght@400;700&family=Montserrat:wght@500&display=swap">
<style>
  :root {
    --backdrop: #2b2b2d;
    --navy: #1c3263;
    --navy-deep: #132550;
    --white: #ffffff;
    --soft-white: #e6ebf5;
  }
  * { margin: 0; padding: 0; box-sizing: border-box; }
  html, body { width: 1200px; height: 900px; overflow: hidden; }
  body {
    background: var(--backdrop);
    position: relative;
    font-family: "Arimo", Arial, sans-serif;
    color: var(--white);
  }
  .card {
    position: absolute;
    width: 600px;
    height: 360px;
    border-radius: 24px;
    overflow: hidden;
    background: linear-gradient(160deg, var(--navy) 0%, var(--navy-deep) 100%);
  }
  .card--back { left: 70px; top: 70px; }
  .card--front { left: 530px; top: 470px; }

  .wordmark {
    position: absolute;
    display: flex;
    align-items: center;
    gap: 14px;
    font-family: "Montserrat", Arial, sans-serif;
    font-weight: 500;
    color: var(--white);
    letter-spacing: 0.14em;
    white-space: nowrap;
  }
  .wordmark__dot {
    width: 14px; height: 14px;
    border-radius: 50%;
    background: var(--white);
  }
  .card--back .wordmark { left: 50%; top: 50%; transform: translate(-50%, -50%); font-size: 36px; }
  .card--front .wordmark { left: 50%; top: 58px; transform: translateX(-50%); font-size: 30px; }

  .identity {
    position: absolute;
    right: 330px;
    top: 152px;
    text-align: right;
  }
  .identity__name {
    font-weight: 700;
    font-size: 24px;
    text-transform: uppercase;
    letter-spacing: 0.01em;
  }
  .identity__role { font-size: 17px; margin-top: 4px; }

  .divider {
    position: absolute;
    left: 290px;
    top: 140px;
    width: 1px;
    height: 80px;
    background: var(--soft-white);
    opacity: 0.8;
  }
  .contacts {
    position: absolute;
    left: 310px;
    top: 138px;
    list-style: none;
    font-size: 16px;
  }
  .contacts__item {
    display: flex;
    align-items: center;
    gap: 10px;
    height: 28px;
  }
  .contacts__icon { width: 16px; height: 16px; flex: none; }

  .license-band {
    position: absolute;
    left: 0;
    right: 0;
    top: 258px;
    height: 40px;
    background: var(--white);
    color: var(--navy-deep);
    font-size: 18px;
    display: flex;
    align-items: center;
    justify-content: flex-end;
    padding-right: 40px;
  }
</style>
</head>
<body>

  <section class="card card--back" aria-label="Card back">
    <div class="wordmark"><span class="wordmark__dot"></span>RVO ELECTRICAL</div>
  </section>

  <section class="card card--front" aria-label="Card front">
    <div class="wordmark"><span class="wordmark__dot"></span>RVO ELECTRICAL</div>

    <div class="identity">
      <p class="identity__name">Gareth Pollwick</p>
      <p class="identity__role">Director</p>
    </div>

    <div class="divider"></div>

    <ul class="contacts">
      <li class="contacts__item">
        <svg class="contacts__icon" viewBox="0 0 16 16" aria-hidden="true">
          <path d="M4 1.5 L6.5 4.5 L5 6.2 C5.8 8 7.8 10 9.8 11 L11.5 9.5 L14.5 12 L12.8 14.3 C7.5 13.8 2.2 8.5 1.7 3.2 Z" fill="var(--white)"/>
        </svg>
        0438 692 174
      </li>
      <li class="contacts__item">
        <svg class="contacts__icon" viewBox="0 0 16 16" aria-hidden="true">
          <rect x="1" y="3" width="14" height="10" rx="1" fill="var(--white)"/>
          <path d="M1.5 3.5 L8 9 L14.5 3.5" fill="none" stroke="var(--navy)" stroke-width="1.3"/>
        </svg>
        admin@rvoelectrical.com.au
      </li>
      <li class="contacts__item">
        <svg class="contacts__icon" viewBox="0 0 16 16" aria-hidden="true">
          <circle cx="8" cy="8" r="7" fill="var(--white)"/>
          <path d="M1 8 H15 M8 1 C5 4 5 12 8 15 M8 1 C11 4 11 12 8 15" fill="none" stroke="var(--navy)" stroke-width="1.1"/>
        </svg>
        www.rvoelectrical.com.au
      </li>
    </ul>

    <div class="license-band">license number - 64139</div>
  </section>

</body>
</html>
```